Brindle painting & waterproofing business card.

Business cards updated to reflect photos attached. we have given the photos of the old business cards and some of our updated designs for other items we have here in the office. Please see attached. if anyone needs to contact us directly for clarification you can email us at brindlerestoration@mailcove.example

Industry/Entity Type

Construction

Contact Information for Business Card

See attached photos

Font styles to use
Other font styles liked:
• Same as photos

Colors
ec1f27

Requirements
Must have
• Employee Names,
• Dennis Marlow II, Supervisor/Owner
• Dee Marlow, President/Owner
• Gus Tremby, Sales Representative
• Lyle Varsen, Supervisor
• Change 20 years to 25
Nice to have
• ideas reflecting the attached photos
Should not have
• should not be exactly like attached photos as those are old business card but reflect to match new logo listed as korvel van and cup photo.

```html
<!DOCTYPE html>
<html lang="en">
<head>
<meta charset="utf-8">
<title>Brindle's Painting &amp; Restoration – Business Card</title>
<link href="https://fonts.googleapis.com/css2?family=Poppins:ital,wght@0,400;0,500;0,600;0,700;1,700&display=swap" rel="stylesheet">
<style>
  :root {
    --brand-orange: #e84e23;
    --card-white: #ffffff;
    --ink: #1f1f1f;
    --ink-soft: #4a4a4a;
    --backdrop: #2a2a2c;
  }
  * { box-sizing: border-box; margin: 0; padding: 0; }
  html, body { width: 1200px; height: 874px; overflow: hidden; }
  body {
    background: var(--backdrop);
    font-family: "Poppins", sans-serif;
    position: relative;
  }
  .card {
    position: absolute;
    width: 640px;
    height: 366px;
    border-radius: 22px;
    overflow: hidden;
  }
  /* Back of card */
  .card-back {
    left: 330px; top: 48px;
    background: var(--brand-orange);
    color: var(--card-white);
    text-align: center;
    padding: 50px 40px 0;
  }
  .card-back .wordmark {
    font-weight: 700;
    font-size: 40px;
    line-height: 1.05;
    letter-spacing: 1px;
    text-transform: uppercase;
  }
  .card-back .wordmark-sub {
    font-weight: 700;
    font-size: 22px;
    letter-spacing: 2px;
    text-transform: uppercase;
    margin-top: 4px;
  }
  .card-back .headline {
    font-weight: 500;
    font-size: 17px;
    line-height: 1.3;
    text-transform: uppercase;
    margin-top: 22px;
  }
  .card-back .services {
    font-size: 13.5px;
    line-height: 1.45;
    margin-top: 12px;
  }
  .card-back .credentials {
    font-weight: 700;
    font-style: italic;
    font-size: 15px;
    margin-top: 16px;
  }
  .anniversary-mark {
    position: absolute;
    right: 26px; top: 110px;
    width: 86px; height: 52px;
    border-radius: 6px;
    background: rgba(255,255,255,0.18);
  }
  /* Front of card */
  .card-front {
    left: 230px; top: 458px;
    background: var(--card-white);
    color: var(--ink);
  }
  .card-front .wordmark {
    position: absolute;
    right: 40px; top: 44px;
    text-align: center;
    font-weight: 700;
    font-size: 30px;
    line-height: 1.05;
    text-transform: uppercase;
    color: var(--ink-soft);
  }
  .card-front .wordmark span { display: block; font-size: 16px; letter-spacing: 1.5px; }
  .person { position: absolute; left: 40px; top: 130px; }
  .person .name {
    font-weight: 600; font-size: 24px; line-height: 1.2; color: var(--brand-orange);
    text-transform: uppercase; letter-spacing: 0.5px;
  }
  .person .role { font-size: 15px; font-weight: 500; line-height: 1.4; }
  .contact-list { list-style: none; margin-top: 10px; font-size: 15px; line-height: 1.4; }
  .contact-list li { display: flex; align-items: center; gap: 8px; }
  .contact-list svg { width: 13px; height: 13px; fill: var(--brand-orange); flex: none; }
  .divider {
    position: absolute; left: 40px; right: 40px; top: 268px;
    border-top: 1px solid var(--ink);
  }
  .address {
    position: absolute; right: 40px; top: 278px;
    text-align: right; font-size: 15px; line-height: 1.35;
  }
  .address .web { color: var(--brand-orange); }
</style>
</head>
<body>

<section class="card card-back">
  <div class="wordmark">Brindle's</div>
  <div class="wordmark-sub">Painting &amp; Restoration</div>
  <p class="headline">Waterproofing &amp; Concrete Restoration<br>Specializing in Hi-Rises &amp; Commercial</p>
  <p class="services">Concrete Restoration • Waterproofing • Painting • Electrostatic<br>Expansion joints • Caulking • Deck Coating • Balustrades &amp; Railing</p>
  <p class="credentials">General Contractor | CGC#0000000 | Licensed &amp; Insured</p>
  <div class="anniversary-mark" role="img" aria-label="Hand-lettered 25 years anniversary mark"></div>
</section>

<section class="card card-front">
  <div class="wordmark">Brindle's<span>Painting &amp; Restoration</span></div>

  <div class="person">
    <div class="name">Dennis Marlow II</div>
    <div class="role">Supervisor / owner</div>
    <ul class="contact-list">
      <li><svg viewBox="0 0 24 24"><path d="M6.6 10.8a15 15 0 0 0 6.6 6.6l2.2-2.2a1 1 0 0 1 1-.25 11.4 11.4 0 0 0 3.6.57 1 1 0 0 1 1 1V20a1 1 0 0 1-1 1A17 17 0 0 1 3 4a1 1 0 0 1 1-1h3.5a1 1 0 0 1 1 1c0 1.25.2 2.45.57 3.57a1 1 0 0 1-.25 1z"/></svg>555.210.4418</li>
      <li><svg viewBox="0 0 24 24"><path d="M7 1h10a2 2 0 0 1 2 2v18a2 2 0 0 1-2 2H7a2 2 0 0 1-2-2V3a2 2 0 0 1 2-2zm0 3v15h10V4z"/></svg>555.368.2097</li>
      <li><svg viewBox="0 0 24 24"><path d="M2 5h20v14H2zm2 2v.5l8 5 8-5V7z"/></svg>brindlerestoration@mailcove.example</li>
    </ul>
  </div>

  <div class="divider"></div>

  <div class="address">
    240 Harbor Reach Ave<br>
    Seabright, FL 30019<br>
    <span class="web">www.brindlerestoration.example</span>
  </div>
</section>

</body>
</html>
```